Wholesale Flyer to mail and drop at Fresh Produce Markets and Stands

We are a small coffee roaster in Tampa Florida, USA. Besides trying to sell coffee to grocery stores and coffee shops, we would like to try to sell coffee to some of the stores and stands that sell mostly just fresh produce. We want to produce a flyer to mail or drop off at stands that sell fresh produce. Can be 8.5" x 11" fold-able to mail or half page postcard design.

Concept
Fresh is the same concept as why people buy from local produce stores and stands - it is very fresh. We sell some of the very best coffee beans - Specialty coffee (see http://www.brevlorn.org/) available. Its the highest quality beans that coffee farmers grow. And it is expensive. Also, we believe that to truly get the best flavor, the coffee should be used within the first 30 days after it is roasted. After that the flavor slowly dissipates.

Most of the stuff in the stores is well over that - even from the local roasters. To differentiate our product and get it to consumers "fresher" we would like to sell via the "fresh Produce" distribution channel.

1) We would like to promote the concept that this is a natural pairing.
Farmers grow it, (its a bean) and it is best fresh
2) Also this product offers a chance for a higher margins than most fresh produce.
3) We have included a copy of a brochure we use and information from that should/can be used,
4) The main reason we are offering designers this project is because we want to show what bags of coffee would look like for sale in a produce stand. (Artists rendering?) This might look rows of vegetables and rows of coffee bags side by side. Some sample pictures are attached.
Once we place product in a few location we might replace or add to this spot - with actual pictures.
5) Also very important is that this picture should include a sign that must say "Roasted On" and a date. (this might be hand written)
6) It should include the coffee's origin or other name such at Ethiopian Coffee or Colombian Coffee.
7) This piece should be mail-able, by folding into 1/3. We will consider both, a flyer we can directly attach a label and one that needs to go in an envelope.
also see www.quillmeadroasting.com for retail site
Updates

Target Market(s)

Fruit and Vegetable Markets

Industry/Entity Type

Food Store

Requirements
Must have
• 1) Information from attached brochure
• 2) We want to show what bags of coffee would look like for sale in a produce stand. (Artists rendering?) This might look rows of vegetables and rows of coffee bags side by side. Some sample pictures are attached of rows of vegetables. FINAL PRODUCT MUST HAVE DRAWING OF ROWS OR GROUPS OF VEGETABLES AND ROWS OR GROUPS OF COFFEE BAGS SIDE BY SIDE - SEE FILE 15- ONE OF THOSE VEGETABLES SHOULD BE BAGS OF COFFEE AND THE SIGN CHANGED TO INCLUDE INFO BELOW
• 3) Also very important is that this picture should include a sign that must say "Roasted On" and a date. (this might be hand written)
• 4) It should include the coffee's origin or other name such at Ethiopian Coffee or Colombian Coffee.
Nice to have
• This product need to fit with other fresh produce - Images of coffee plant and or farm.
Should not have
• Anything to do with cupping the coffee

```html
<!DOCTYPE html>
<html lang="en">
<head>
<meta charset="utf-8">
<title>Quillmead Roasting – Freshest Coffee Flyer</title>
<link rel="stylesheet" href="https://fonts.googleapis.com/css2?family=Oswald:wght@400;600;700&family=Open+Sans:wght@400;600;700&family=Kalam:wght@400&display=swap">
<style>
  :root {
    --espresso: #2e1c13;
    --roast: #4a2e1f;
    --burlap: #a98460;
    --burlap-light: #d3b690;
    --kraft: #b8956a;
    --lime: #b9d34a;
    --leaf: #5c7a23;
    --cream: #ffffff;
    --paper: #fbfaf7;
    --panel: rgba(40, 24, 16, 0.82);
    --ink: #4a4038;
  }
  * { box-sizing: border-box; margin: 0; padding: 0; }
  html, body { width: 857px; height: 1200px; overflow: hidden; background: var(--paper); }
  body { font-family: "Open Sans", Arial, sans-serif; color: var(--ink); }

  .flyer { position: relative; width: 857px; height: 1200px; background: var(--paper); overflow: hidden; }

  .hero-photo {
    position: absolute; left: 0; top: 0; width: 857px; height: 600px;
    background: linear-gradient(160deg, var(--roast) 0%, var(--burlap) 45%, var(--burlap-light) 75%, var(--paper) 100%);
  }
  .hero-shade {
    position: absolute; left: 0; top: 0; width: 520px; height: 520px;
    background: linear-gradient(90deg, rgba(30,18,12,0.8) 0%, rgba(30,18,12,0.5) 70%, rgba(30,18,12,0) 100%);
  }

  .headline { position: absolute; left: 36px; top: 92px; color: var(--cream); font-family: "Oswald", Arial, sans-serif; text-transform: uppercase; }
  .headline .kicker { font-size: 44px; font-weight: 400; letter-spacing: 1px; line-height: 1; }
  .headline .main { display: flex; align-items: baseline; gap: 10px; margin-top: 4px; }
  .headline .big { font-size: 112px; font-weight: 700; line-height: 0.95; letter-spacing: 1px; }
  .headline .is { font-size: 44px; font-weight: 400; }
  .headline .sub { font-size: 38px; font-weight: 400; line-height: 1.1; letter-spacing: 0.5px; }

  .intro { position: absolute; left: 36px; top: 318px; width: 420px; color: var(--cream); font-size: 20px; line-height: 1.4; }

  .feature-panel {
    position: absolute; left: 478px; top: 100px; width: 350px; height: 420px;
    background: var(--panel); color: var(--cream); padding: 22px 24px;
  }
  .feature-panel h2 { font-size: 25px; font-weight: 600; line-height: 1.2; margin-bottom: 6px; }
  .feature-panel .lead { font-size: 17px; line-height: 1.35; margin-bottom: 16px; }
  .feature-list { list-style: none; }
  .feature-list li { font-size: 15px; line-height: 1.4; margin-bottom: 14px; color: #e9ddd1; }

  .stand-scene {
    position: absolute; left: 0; top: 520px; width: 857px; height: 400px;
    background:
      radial-gradient(ellipse at 74% 62%, #5a341d 0%, #7b4a2a 30%, rgba(180,140,100,0.35) 58%, rgba(251,250,247,0) 78%),
      linear-gradient(90deg, #8ea65a 0%, #b59368 26%, #c9a77a 40%, var(--paper) 55%, var(--paper) 100%);
  }

  .roast-sign {
    position: absolute; left: 300px; top: 700px; width: 150px; height: 96px;
    background: var(--kraft); border: 3px solid var(--roast);
    text-align: center; padding-top: 10px; color: var(--espresso);
    font-family: "Kalam", cursive;
  }
  .roast-sign .label { font-size: 22px; line-height: 1.1; }
  .roast-sign .date { font-size: 26px; line-height: 1.2; }

  .brand { position: absolute; left: 110px; top: 945px; display: flex; align-items: center; gap: 12px; }
  .brand .mark { width: 36px; height: 36px; border-radius: 50%; background: var(--roast); }
  .brand .name { font-size: 30px; font-weight: 600; color: var(--roast); }

  .contact { position: absolute; left: 40px; top: 1010px; width: 400px; text-align: center; }
  .contact .address { font-size: 14px; color: var(--ink); letter-spacing: 0.5px; }
  .contact .phone { font-family: "Oswald", Arial, sans-serif; font-size: 52px; font-weight: 600; color: var(--leaf); line-height: 1.15; letter-spacing: 1px; }
  .contact .web { font-size: 18px; color: var(--roast); letter-spacing: 1px; }

  .origin { position: absolute; left: 478px; top: 945px; width: 350px; }
  .origin h3 { font-size: 32px; font-weight: 700; color: var(--leaf); line-height: 1.1; margin-bottom: 12px; }
  .origin p { font-size: 15px; line-height: 1.45; color: var(--ink); }
</style>
</head>
<body>
<main class="flyer">
  <div class="hero-photo" role="img" aria-label="Close-up photo of a burlap sack filled with roasted coffee beans"></div>
  <div class="hero-shade"></div>

  <header class="headline">
    <div class="kicker">The Best</div>
    <div class="main"><span class="big">Coffee</span><span class="is">is</span></div>
    <div class="sub">The Freshest Coffee</div>
  </header>

  <p class="intro">Coffee beans, like other crops change with the season and are best fresh. The very best coffee should be sold as produce not as a can good.</p>

  <section class="feature-panel">
    <h2>Locally Roasted in Tampa</h2>
    <p class="lead">Fresh – Roasted 24-48 hours before Delivery – Date on Bag</p>
    <ul class="feature-list">
      <li>Single Origin Specialty Coffee Beans of rated Excellent to Outstanding (Brevlorn standards)</li>
      <li>Beans rotated out every 3 weeks No charge and buy back guarantee</li>
      <li>Morning Brews and Espresso Blends available in 12 oz. Kraft bags and 16 oz. Pouches</li>
    </ul>
  </section>

  <div class="stand-scene" role="img" aria-label="Produce stand with rows of vegetables beside rows of kraft coffee bags and a pile of roasted beans"></div>

  <div class="roast-sign">
    <div class="label">Roasted On</div>
    <div class="date">10/14</div>
  </div>

  <div class="brand">
    <span class="mark"></span>
    <span class="name">Quillmead Roasting</span>
  </div>

  <footer class="contact">
    <div class="address">4410 Harbor Ave, Tampa FL 33601</div>
    <div class="phone">727.555.0142</div>
    <div class="web">www.quillmeadroasting.com</div>
  </footer>

  <section class="origin">
    <h3>Colombian Coffee</h3>
    <p>Beans are seasonal: Origins Change, this benefits customers that like Variety. However, morning and espresso blends stay the same for customer that prefer consistency.</p>
  </section>
</main>
</body>
</html>
```